Cobalt Homes Web Site Design

improve on the graphic design on our current website
www.cobalthmoes.com.au
wordpress required

Graphic Design

Coding

Coded - Design and coding required

Number of Pages Required

5+ page

```html
<!DOCTYPE html>
<html lang="en">
<head>
<meta charset="utf-8">
<title>Cobalt Homes &amp; Designs</title>
<link href="https://fonts.googleapis.com/css2?family=Raleway:wght@400;500;600;700&family=Open+Sans:wght@400;600&display=swap" rel="stylesheet">
<style>
:root{
  --red:#c8161d;
  --red-dark:#a10f15;
  --ink:#222222;
  --text:#555555;
  --muted:#8a8a8a;
  --line:#e2e2e2;
  --paper:#ffffff;
  --soft:#f3f3f3;
  --dark:#1f1f1f;
  --darker:#151515;
}
*{box-sizing:border-box;margin:0;padding:0}
html,body{width:1200px;height:3939px;overflow:hidden}
body{font-family:"Raleway",sans-serif;color:var(--text);background:var(--paper);position:relative}
.abs{position:absolute}
.btn{display:inline-flex;align-items:center;justify-content:center;background:var(--red);color:#fff;font-family:"Raleway",sans-serif;font-size:15px;font-weight:500;border-radius:2px}
.section-title{position:absolute;left:0;width:1200px;text-align:center;font-size:27px;font-weight:500;color:var(--ink);letter-spacing:.5px}
.section-title span{color:var(--red)}
.title-rule{position:absolute;left:576px;width:48px;height:3px;background:var(--red)}

/* header */
.topline{top:0;left:0;width:1200px;height:4px;background:var(--red)}
.site-header{top:4px;left:0;width:1200px;height:114px;background:var(--paper)}
.brand{position:absolute;left:100px;top:24px;display:flex;align-items:center;gap:12px}
.brand-dot{width:44px;height:44px;border-radius:50%;background:var(--red)}
.brand-name{font-size:30px;font-weight:600;color:var(--ink);line-height:1}
.brand-sub{font-size:10px;color:var(--muted);margin-top:4px}
.main-nav{position:absolute;left:468px;top:44px;display:flex;gap:0;font-size:14px;color:var(--ink)}
.main-nav a{margin-right:40px;text-decoration:none;color:var(--ink)}
.main-nav a.current{color:var(--red)}
.nav-icons{position:absolute;left:1045px;top:44px;display:flex;gap:18px}

/* hero */
.hero{top:118px;left:0;width:1200px;height:486px;background:linear-gradient(180deg,#4b5664 0%,#39414c 45%,#2b2e33 80%,#4a4740 100%)}
.hero-copy{position:absolute;top:150px;left:0;width:1200px;text-align:center;color:#fff}
.hero-copy h1{font-size:36px;font-weight:600;line-height:1.35;letter-spacing:.5px}
.hero-copy h1 .big{display:block;font-size:48px;font-weight:700}
.hero-copy p{font-size:26px;font-weight:600;margin-top:14px}
.hero .btn{position:absolute;left:512px;top:347px;width:158px;height:47px;font-size:17px;border:1px solid #fff}
.hero-arrow{position:absolute;top:258px;width:44px;height:44px;border-radius:50%;background:rgba(0,0,0,.55);display:flex;align-items:center;justify-content:center}

/* info bar */
.info-bar{top:630px;left:100px;width:1003px;height:84px;display:flex;box-shadow:0 2px 8px rgba(0,0,0,.12)}
.info-item{flex:1;display:flex;align-items:center;gap:22px;padding-left:30px;background:var(--paper);font-size:14px;color:var(--text);line-height:1.5}
.info-item.phone{background:var(--red);color:#fff;flex:0 0 320px}
.info-item .sep{width:1px;height:50px;background:var(--line)}

/* why */
.why-sub{position:absolute;top:832px;width:1200px;text-align:center;font-size:14px;color:var(--muted)}
.why-photo{top:888px;left:100px;width:399px;height:346px;border-radius:0 0 60px 0;background:linear-gradient(160deg,#a9c6e4 0%,#dfe8ef 45%,#6b9a4f 75%,#3d7438 100%)}
.why-lead{top:884px;left:559px;width:545px;font-size:19px;line-height:1.45;color:var(--ink)}
.why-lead span{color:var(--red)}
.why-list{top:985px;left:559px;width:545px;font-size:13px;line-height:26px;color:var(--text);list-style:none}
.why-list li::before{content:attr(data-n) ".  "}
.why-rule{top:1116px;left:559px;width:545px;height:2px;background:var(--red)}
.feature{position:absolute;top:1142px;display:flex;gap:18px;width:260px}
.feature h3{font-size:15px;font-weight:500;color:var(--ink);margin-bottom:6px}
.feature p{font-size:11px;line-height:1.5;color:var(--muted)}

/* service */
.service{top:1284px;left:0;width:1200px;height:507px;background:linear-gradient(180deg,#2a2a2a,#1b1b1b)}
.service .section-title{top:50px;color:#fff}
.service .title-rule{top:94px}
.service-card{position:absolute;top:134px;width:300px;text-align:center;color:#fff}
.service-icon{width:158px;height:158px;margin:0 auto;border-radius:50%;border:3px solid #fff;display:flex;align-items:center;justify-content:center}
.service-icon .inner{width:132px;height:132px;border-radius:50%;background:var(--paper);display:flex;align-items:center;justify-content:center}
.service-card h3{font-size:16px;font-weight:500;margin-top:28px}
.service-card p{font-size:12px;line-height:1.65;color:#cfcfcf;margin:12px 22px 0}
.service-card .btn{width:110px;height:40px;margin-top:20px;font-size:13px}

/* portfolio */
.filters{top:1920px;left:278px;display:flex;gap:13px}
.filters span{height:31px;padding:0 22px;display:flex;align-items:center;background:#2b2b2b;color:#fff;font-size:13px}
.filters span.on{background:var(--red)}
.grid{top:1990px;left:0;width:1200px;height:481px;display:grid;grid-template-columns:repeat(4,1fr);grid-template-rows:repeat(2,1fr)}
.tile{position:relative}
.t1{background:linear-gradient(170deg,#8fb5d6,#c8b59a 55%,#577a3c)}
.t2{background:linear-gradient(170deg,#5b73a8,#d7dbe2 55%,#7a8391)}
.t3{background:linear-gradient(170deg,#b7cde0,#f1f1ef 55%,#7f9a66)}
.t4{background:linear-gradient(170deg,#7fa8cf,#c6b49b 50%,#3aa0b5)}
.t5{background:linear-gradient(170deg,#cfd9e4,#6d7479 55%,#3e9fd0)}
.t6{background:var(--red);display:flex;flex-direction:column;align-items:center;justify-content:center;color:#fff;text-align:center}
.t6 .show{border:1px solid #fff;padding:9px 18px;font-size:13px;margin-bottom:30px}
.t6 h4{font-size:17px;font-weight:500;line-height:1.45}
.t7{background:linear-gradient(170deg,#8fc0ec,#d8d2c4 50%,#4e8a2f)}
.t8{background:linear-gradient(170deg,#3b4f8e,#6b6f86 55%,#2f3640)}

.quote-band{top:2471px;left:0;width:1200px;height:129px;background:var(--soft)}
.quote-band p{position:absolute;left:100px;top:50px;font-size:22px;color:var(--ink)}
.quote-band .btn{position:absolute;left:866px;top:42px;width:184px;height:47px;font-size:15px}

/* team */
.team-photo{top:2723px;width:208px;height:231px;background:linear-gradient(180deg,#d9d9d9,#8f8f8f);border:2px solid #fff;box-shadow:0 0 0 1px var(--line)}
.member{position:absolute;top:2730px;width:250px;font-size:12px;line-height:1.6;color:var(--muted)}
.member h3{font-size:17px;font-weight:600;color:var(--ink)}
.member .role{font-size:13px;color:var(--text);margin:6px 0 12px}
.member.left{left:97px;text-align:right}
.member.right{left:853px}
.socials{display:flex;gap:14px;margin-top:26px}
.member.left .socials{justify-content:flex-end}
.socials i{width:30px;height:30px;border-radius:50%;border:1px solid var(--red);display:flex;align-items:center;justify-content:center}
.socials i::after{content:"";width:8px;height:8px;border-radius:50%;background:var(--red)}

/* testimonials */
.testimonials{top:2973px;left:0;width:1200px;height:475px;background:var(--soft)}
.testimonials .section-title{top:48px}
.testimonials .title-rule{top:88px}
.testimonials .sub{position:absolute;top:118px;width:1200px;text-align:center;font-size:15px;color:var(--text)}
.t-card{position:absolute;top:152px;width:315px;height:263px;background:var(--paper);padding:26px 20px;box-shadow:0 1px 4px rgba(0,0,0,.08)}
.t-mark{width:34px;height:34px;background:var(--red);color:#fff;font-family:Georgia,serif;font-size:30px;font-weight:700;display:flex;align-items:center;justify-content:center;line-height:1;padding-top:12px}
.t-card h4{font-size:14px;font-weight:600;color:var(--ink);margin:18px 0 10px;text-transform:uppercase}
.t-card p{font-size:12px;line-height:1.7;color:var(--muted)}
.t-author{position:absolute;left:20px;bottom:24px;display:flex;align-items:center;gap:12px;font-size:13px;color:var(--ink)}
.t-author .av{width:34px;height:34px;background:#c9c9c9}
.stars{color:#f0b400;font-size:11px;letter-spacing:1px}
.t-nav{position:absolute;top:278px;font-size:30px;color:#aaa}

/* cta */
.cta{top:3448px;left:0;width:1200px;height:84px;background:#efefef}
.cta-red{position:absolute;left:0;top:0;width:530px;height:84px;background:var(--red);clip-path:polygon(0 0,100% 0,86% 100%,0 100%)}
.cta-red small{position:absolute;left:100px;top:18px;font-size:12px;color:#fff;font-weight:600}
.cta-red strong{position:absolute;left:100px;top:40px;font-size:21px;color:#fff;font-weight:500}
.newsletter{position:absolute;left:558px;top:18px;color:var(--ink)}
.newsletter b{display:block;font-size:21px;font-weight:500}
.newsletter span{font-size:13px}
.news-input{position:absolute;left:788px;top:23px;width:260px;height:42px;background:#fff;border:1px solid var(--line);font-size:12px;color:#aaa;padding:13px 14px}
.news-btn{position:absolute;left:1048px;top:23px;width:52px;height:42px}

/* footer */
.footer{top:3532px;left:0;width:1200px;height:407px;background:linear-gradient(180deg,#1c1c1c,var(--darker))}
.footer h2{position:absolute;left:100px;top:44px;font-size:21px;font-weight:600;color:#fff}
.footer .blurb{position:absolute;left:100px;top:86px;width:550px;font-size:11px;line-height:1.7;color:#8e8e8e}
.field{position:absolute;height:38px;border:1px solid #3a3a3a;font-size:12px;color:#777;padding:11px 12px}
.footer .btn.send{position:absolute;left:383px;top:257px;width:271px;height:38px}
.f-social{position:absolute;display:flex;align-items:center;gap:16px;font-size:15px;color:#bdbdbd}
.f-social i{width:44px;height:44px;border-radius:50%;background:#2c2c2c;display:block}
.f-rule{position:absolute;left:720px;top:213px;width:383px;height:1px;background:#333}
.f-contact{position:absolute;top:262px;display:flex;align-items:center;gap:12px;font-size:12px;color:#9a9a9a}
.copyright{position:absolute;left:0;top:352px;width:1200px;text-align:center;font-size:11px;color:#777}
</style>
</head>
<body>

<div class="abs topline"></div>
<header class="abs site-header">
  <div class="brand">
    <div class="brand-dot"></div>
    <div>
      <div class="brand-name">Cobalt Homes</div>
      <div class="brand-sub">Homes &amp; Designs Pty Ltd</div>
    </div>
  </div>
  <nav class="main-nav">
    <a class="current">Home</a><a>Company</a><a>Excellence</a><a>Experience</a><a>Expertise</a><a>Contact</a>
  </nav>
  <div class="nav-icons">
    <svg width="16" height="16" viewBox="0 0 16 16" fill="none" stroke="#777" stroke-width="1.4"><path d="M1 2h2l2 8h8l2-6H4"/><circle cx="6" cy="13.5" r="1.2"/><circle cx="12" cy="13.5" r="1.2"/></svg>
    <svg width="15" height="15" viewBox="0 0 16 16" fill="none" stroke="#777" stroke-width="1.5"><circle cx="6.5" cy="6.5" r="5"/><path d="M10.5 10.5 15 15"/></svg>
  </div>
</header>

<section class="abs hero" role="img" aria-label="Dusk photograph of a modern glass office building">
  <div class="hero-copy">
    <h1>WELCOME TO<span class="big">COBALT HOMES &amp; DESIGNS</span></h1>
    <p>We Are Architecture + Construction</p>
  </div>
  <span class="btn">Read More</span>
  <div class="hero-arrow" style="left:26px"><svg width="12" height="16" viewBox="0 0 12 16"><path d="M9 2 3 8l6 6" stroke="#fff" stroke-width="2" fill="none"/></svg></div>
  <div class="hero-arrow" style="left:1128px"><svg width="12" height="16" viewBox="0 0 12 16"><path d="M3 2l6 6-6 6" stroke="#fff" stroke-width="2" fill="none"/></svg></div>
</section>

<div class="abs info-bar">
  <div class="info-item">
    <svg width="26" height="34" viewBox="0 0 26 34" fill="none" stroke="var(--red)" stroke-width="2.2"><path d="M13 32S3 19 3 12a10 10 0 0 1 20 0c0 7-10 20-10 20z"/><circle cx="13" cy="12" r="4"/></svg>
    <div class="sep"></div>
    <div>42 Harlow Cres.,<br>Kingsford , Canberra ACT</div>
  </div>
  <div class="info-item phone">
    <svg width="34" height="34" viewBox="0 0 24 24" fill="none" stroke="#fff" stroke-width="1.6"><path d="M5 3h4l2 5-3 2a12 12 0 0 0 6 6l2-3 5 2v4a2 2 0 0 1-2 2A17 17 0 0 1 3 5a2 2 0 0 1 2-2z"/></svg>
    <div class="sep" style="background:rgba(255,255,255,.4)"></div>
    <div>Tel: 0400 555 218</div>
  </div>
  <div class="info-item">
    <svg width="30" height="30" viewBox="0 0 30 30" fill="none" stroke="var(--red)" stroke-width="2.2"><circle cx="15" cy="15" r="12"/><path d="M15 8v7l5 3"/></svg>
    <div class="sep"></div>
    <div>Week Days: 07:00 – 19:00<br>Sat day : Sunday: 09:00 – 15:00</div>
  </div>
</div>

<h2 class="section-title" style="top:764px">WHY <span>COBALT</span> HOMES?</h2>
<div class="abs title-rule" style="top:806px"></div>
<p class="why-sub">Our vision is to build homes</p>
<div class="abs why-photo" role="img" aria-label="Photograph of a white modern house with a pool and lawn"></div>
<p class="abs why-lead"><span>We're a boutique building company</span> in Canberra, that has built many residential properties.</p>
<ul class="abs why-list">
  <li data-n="1">It is a long established fact that a reader will be distracted</li>
  <li data-n="2">Being in the industry for many years has enabled us to master</li>
  <li data-n="3">The art of designing and constructing stylish homes.</li>
  <li data-n="4">That are not only aesthetically pleasing but also affordable.</li>
</ul>
<div class="abs why-rule"></div>
<div class="feature" style="left:559px">
  <svg width="42" height="38" viewBox="0 0 42 38" fill="none" stroke="#666" stroke-width="2"><path d="M2 3h6l5 21h22l5-15H10"/><circle cx="16" cy="32" r="3"/><circle cx="32" cy="32" r="3"/></svg>
  <div><h3>Our Shop</h3><p>Contrary to popular belief, Lorem Ipsum is not simply random</p></div>
</div>
<div class="feature" style="left:842px">
  <svg width="40" height="40" viewBox="0 0 40 40" fill="none" stroke="#666" stroke-width="2"><circle cx="20" cy="13" r="9"/><path d="M3 38c1-9 8-14 17-14s16 5 17 14"/></svg>
  <div><h3>Our Profile</h3><p>Contrary to popular belief, Lorem Ipsum is not simply random</p></div>
</div>

<section class="abs service">
  <h2 class="section-title">OUR <span>SERVICE</span></h2>
  <div class="title-rule"></div>
  <div class="service-card" style="left:94px">
    <div class="service-icon"><div class="inner">
      <svg width="60" height="56" viewBox="0 0 60 56" fill="var(--dark)"><rect x="4" y="20" width="14" height="34"/><rect x="22" y="6" width="16" height="48"/><rect x="42" y="26" width="14" height="28"/><rect x="0" y="53" width="60" height="3"/></svg>
    </div></div>
    <h3>Canberra Building Services</h3>
    <p>Cobalt Homes is a Canberra based building company focusing on first class residential homes</p>
    <span class="btn">Read More</span>
  </div>
  <div class="service-card" style="left:443px">
    <div class="service-icon"><div class="inner">
      <svg width="60" height="60" viewBox="0 0 60 60" fill="var(--dark)"><rect x="26" y="-4" width="10" height="68" transform="rotate(45 30 30)"/><rect x="24" y="-4" width="12" height="68" transform="rotate(-45 30 30)"/></svg>
    </div></div>
    <h3>Top Class Architects</h3>
    <p>Cobalt Homes is a Canberra based building company focusing on first class residential homes</p>
    <span class="btn">Read More</span>
  </div>
  <div class="service-card" style="left:793px">
    <div class="service-icon"><div class="inner">
      <svg width="64" height="52" viewBox="0 0 64 52" fill="var(--dark)"><rect x="8" y="16" width="26" height="18"/><rect x="4" y="36" width="36" height="10" rx="5"/><path d="M34 20 50 6l10 14-4 3-7-8-13 10z"/><path d="M54 22h8l-2 10h-8z"/></svg>
    </div></div>
    <h3>Reliable Contractors</h3>
    <p>Cobalt Homes is a Canberra based building company focusing on first class residential homes</p>
    <span class="btn">Read More</span>
  </div>
</section>

<h2 class="section-title" style="top:1841px">OUR <span>PORTFOLIO</span></h2>
<div class="abs title-rule" style="top:1882px"></div>
<div class="abs filters">
  <span class="on">Show All</span><span>Gallery</span><span>Builder</span><span>Extensions</span><span>Bathrooms</span><span>Refurbishment</span>
</div>
<div class="abs grid">
  <div class="tile t1" role="img" aria-label="Photograph of a two-storey family home with front garden"></div>
  <div class="tile t2" role="img" aria-label="Photograph of a modern white house lit at dusk"></div>
  <div class="tile t3" role="img" aria-label="Photograph of a white contemporary house with lawn"></div>
  <div class="tile t4" role="img" aria-label="Photograph of a resort-style pool terrace"></div>
  <div class="tile t5" role="img" aria-label="Photograph of a modern house beside a pool"></div>
  <div class="tile t6"><span class="show">Show All</span><h4>OUR LIBRARY IS GREAT<br>TREASURE</h4></div>
  <div class="tile t7" role="img" aria-label="Photograph of a suburban house with green lawn"></div>
  <div class="tile t8" role="img" aria-label="Photograph of a dark modern house at twilight"></div>
</div>

<div class="abs quote-band">
  <p>Get a FREE building estimation today for your next project!</p>
  <span class="btn">Get Me The Quote</span>
</div>

<h2 class="section-title" style="top:2645px">MEET OUR <span>TEAM</span></h2>
<div class="abs title-rule" style="top:2686px"></div>
<div class="member left">
  <h3>Maren Holt</h3>
  <div class="role">Architect</div>
  <p>Mauris accumsan eros eget libero posuere vulputate. Etiam elit elit, elementum sed varius at, adipiscing vitae est.</p>
  <div class="socials"><i></i><i></i><i></i></div>
</div>
<div class="abs team-photo" style="left:386px" role="img" aria-label="Portrait photograph of the architect"></div>
<div class="abs team-photo" style="left:609px" role="img" aria-label="Portrait photograph of the CEO"></div>
<div class="member right">
  <h3>Gideon Price</h3>
  <div class="role">CEO &amp; Architect</div>
  <p>Mauris accumsan eros eget libero posuere vulputate. Etiam elit elit, elementum sed varius at, adipiscing vitae est.</p>
  <div class="socials"><i></i><i></i><i></i></div>
</div>

<section class="abs testimonials">
  <h2 class="section-title">OUR <span>CLENT TESTIMONIAL</span></h2>
  <div class="title-rule"></div>
  <p class="sub">What Our Client Says About Us</p>
  <span class="t-nav" style="left:44px">&#8249;</span>
  <span class="t-nav" style="left:1136px">&#8250;</span>
  <div class="t-card" style="left:100px">
    <div class="t-mark">&#8220;</div>
    <h4>Knowledge is Knowledge</h4>
    <p>I've engaged Cobalt Homes to build my first house in Canberra, all I can say is they've been fantastic. Sam has helped me out at every</p>
    <div class="t-author"><span class="av"></span><div>Clara Benning<div class="stars">★★★★★</div></div></div>
  </div>
  <div class="t-card" style="left:444px">
    <div class="t-mark">&#8220;</div>
    <h4>Create with the Heart</h4>
    <p>I would like to thank Cobalt Homes for being a part of my investment property. I don't live in Canberra, so it's a little</p>
    <div class="t-author"><span class="av"></span><div>Owen Rask<div class="stars">★★★★★</div></div></div>
  </div>
  <div class="t-card" style="left:788px">
    <div class="t-mark">&#8220;</div>
    <h4>We are all Constructed</h4>
    <p>Great team and excellent services. I'm very pleased with the way my house turned out. It's been a pleasure working with you guys</p>
    <div class="t-author"><span class="av"></span><div>Ravi Talwar<div class="stars">★★★★★</div></div></div>
  </div>
</section>

<div class="abs cta">
  <div class="cta-red"><small>Can We Help ?</small><strong>Contact us on 0400 555 218</strong></div>
  <div class="newsletter"><b>Newsletter Signup</b><span>Latest News and Updates</span></div>
  <div class="news-input">Email id</div>
  <span class="btn news-btn">Go</span>
</div>

<footer class="abs footer">
  <h2>CONTACT US</h2>
  <p class="blurb">Curabitur at lectus hendrerit, suscipit ante nec, blandit enim. Aliquam lacinia, enim non rutrum egestas, turpis orci gravida dolor, vitae rhoncus quam felis nec justo. Sed et viverra velit.</p>
  <div class="field" style="left:100px;top:158px;width:271px">Your Name</div>
  <div class="field" style="left:100px;top:207px;width:271px">Your Mail Id</div>
  <div class="field" style="left:100px;top:257px;width:271px">Your Phone Number</div>
  <div class="field" style="left:383px;top:158px;width:271px;height:87px">Your Message</div>
  <span class="btn send">Send Now</span>
  <div class="f-social" style="left:720px;top:75px"><i></i>Pagebook</div>
  <div class="f-social" style="left:884px;top:75px"><i></i>Chirper</div>
  <div class="f-social" style="left:720px;top:143px"><i></i>Searchly</div>
  <div class="f-social" style="left:884px;top:143px"><i></i>Snapgram</div>
  <div class="f-rule"></div>
  <div class="f-contact" style="left:720px">
    <svg width="16" height="12" viewBox="0 0 16 12" fill="none" stroke="#9a9a9a" stroke-width="1.3"><rect x="1" y="1" width="14" height="10"/><path d="m1 1 7 6 7-6"/></svg>
    hello@cobalthomes.example
  </div>
  <div class="f-contact" style="left:918px">
    <svg width="14" height="14" viewBox="0 0 24 24" fill="none" stroke="#9a9a9a" stroke-width="2"><path d="M5 3h4l2 5-3 2a12 12 0 0 0 6 6l2-3 5 2v4a2 2 0 0 1-2 2A17 17 0 0 1 3 5a2 2 0 0 1 2-2z"/></svg>
    (02) 6100 555 030
  </div>
  <p class="copyright">Copyright@2016companyname . All Rights Reserved.</p>
</footer>

</body>
</html>
```